Veranta - Solution provider in business consulting

Veranta is a swiss based company providing solutions for developing markets. The business covers various fields of business consulting, such as supply chain, product costs, quality management and manufacturing management. The Business operates in a efficient, straight and solution oriented manner.
The final design should communicate these characteristics. Asian people as well as as western people shall identify the qualities of the company at first sight.
The customer needs business cards with a simple view but an recognizable design, printed in high quality. Engraved elements such as the globe or simple words are possible.
Available colors are: (RAL)
102/102/102
51/102/102
153/204/153
255/102/51
Font: Calibri
Industry/Entity Type
Business
Look and feel
Each slider illustrates characteristics of the customer's brand and the style your logo design should communicate.

```html
<!DOCTYPE html>
<html lang="en">
<head>
<meta charset="utf-8">
<title>Veranta – Business Card</title>
<link href="https://fonts.googleapis.com/css2?family=Carlito:wght@400;700&display=swap" rel="stylesheet">
<style>
  :root {
    --stage: #e8e8e5;
    --card: #f4f4f3;
    --grey: #666666;
    --teal: #336666;
    --orange: #ec6a3f;
    --white: #ffffff;
  }
  * { box-sizing: border-box; margin: 0; padding: 0; }
  html, body {
    width: 1200px; height: 1200px; overflow: hidden;
    background: var(--stage);
    font-family: "Carlito", sans-serif;
  }
  .card {
    position: absolute; left: 100px; top: 330px;
    width: 1000px; height: 540px;
    background: var(--card);
    box-shadow: 0 6px 24px rgba(0,0,0,0.12);
    overflow: hidden;
  }
  .card-shapes { position: absolute; inset: 0; width: 1000px; height: 540px; }
  .shape-teal { fill: var(--teal); }
  .shape-orange { fill: var(--orange); }

  .brand {
    position: absolute; left: 62px; top: 92px;
    display: flex; align-items: center; gap: 22px;
    color: var(--grey); font-size: 84px; font-weight: 400; letter-spacing: 1px;
  }
  .brand-dot { width: 64px; height: 64px; border-radius: 50%; background: var(--grey); }

  .person {
    position: absolute; right: 50px; top: 104px;
    text-align: right; color: var(--white);
  }
  .person-name { font-size: 30px; font-weight: 700; line-height: 1; }
  .person-role { font-size: 15px; margin-top: 4px; }

  .contacts {
    position: absolute; right: 45px; top: 180px;
    list-style: none; color: var(--grey);
    font-size: 28px; line-height: 38px; text-align: right;
  }
  .contacts li { display: flex; justify-content: flex-end; align-items: center; gap: 12px; }
  .contacts svg { width: 24px; height: 24px; fill: var(--teal); flex: none; }

  .address {
    position: absolute; left: 60px; top: 340px;
    color: var(--white); font-size: 28px; line-height: 38px;
  }
  .address-company { font-weight: 700; }
</style>
</head>
<body>
  <main class="card">
    <svg class="card-shapes" viewBox="0 0 1000 540" aria-hidden="true">
      <polygon class="shape-teal" points="0,290 500,290 330,540 0,540"/>
      <polygon class="shape-orange" points="572,92 960,92 960,152 531,152"/>
    </svg>

    <div class="brand">
      <span class="brand-name">veranta</span>
      <span class="brand-dot"></span>
    </div>

    <div class="person">
      <p class="person-name">Marco Heller</p>
      <p class="person-role">CEO</p>
    </div>

    <ul class="contacts">
      <li>+41 79 305 2718
        <svg viewBox="0 0 24 24"><path d="M6 1h12a1 1 0 0 1 1 1v20a1 1 0 0 1-1 1H6a1 1 0 0 1-1-1V2a1 1 0 0 1 1-1zm1 3v9h10V4zm1 11v2h2v-2zm3 0v2h2v-2zm3 0v2h2v-2zM8 18v2h2v-2zm3 0v2h2v-2zm3 0v2h2v-2z"/></svg>
      </li>
      <li>+41 71 840 3196
        <svg viewBox="0 0 24 24"><path d="M2 7c0-2 4-4 10-4s10 2 10 4v2h-5V7.5c-1-.6-3-1-5-1s-4 .4-5 1V9H2zm4 4h12l3 8v2H3v-2zm6 2a3 3 0 1 0 0 6 3 3 0 0 0 0-6z"/></svg>
      </li>
      <li>marco.heller@veranta.ch
        <svg viewBox="0 0 24 24"><path d="M2 5h20v14H2zm2 2v.5l8 6 8-6V7zm0 3v7h16v-7l-8 6z"/></svg>
      </li>
      <li>www.veranta.ch
        <svg viewBox="0 0 24 24"><path d="M12 2a10 10 0 1 0 0 20 10 10 0 0 0 0-20zm-1 2.1V8H7.6A8 8 0 0 1 11 4.1zm2 0A8 8 0 0 1 16.4 8H13zM6.6 10H11v4H6.6a8 8 0 0 1 0-4zM13 10h4.4a8 8 0 0 1 0 4H13zm-5.4 6H11v3.9A8 8 0 0 1 7.6 16zm5.4 0h3.4a8 8 0 0 1-3.4 3.9z"/></svg>
      </li>
    </ul>

    <address class="address" style="font-style: normal;">
      <p class="address-company">Veranta GmbH</p>
      <p>Feldrain 14</p>
      <p>9246 Niederau</p>
      <p>Switzerland</p>
    </address>
  </main>
</body>
</html>
```